Journal Cover Design Project

The Meridian Review of Rising Trade Nations is a professional journal which aims to provide an international platform for publication of original research on the emerging economies.
The journal is published three times a year and available by subscription. Currently, the cover design is the same for each issue. We are looking to redesign the cover (and interior) of our journal and would like a design that would allow us to change the color scheme for each issue or volume while maintaining a consistent design scheme.
Our design preference is simple and modern with good use of color. Many of our past publications have used abstract maps/globes but we are open to new ideas. We would need a creative way to include text on the cover, possibly a way to present the article titles or main topics for each issue. For example, we like the use of color and the general design in this image: http://www.pictavo-share.example/photos/brightmakerstudio/5120448391/lightbox/
Below is a link to our most recent issue of the journal. You can see an example of the article titles, structure, etc. The website also shows the current cover of the journal (but we do not want the new design to be based off of the current one):
http://mrt.quellpress.example/content/4/2.toc

```html
<!DOCTYPE html>
<html lang="en">
<head>
<meta charset="utf-8">
<title>MRRTN – Journal Cover</title>
<link rel="stylesheet" href="https://fonts.googleapis.com/css2?family=Open+Sans:wght@400;600;700&family=Barlow+Condensed:wght@600;700&display=swap">
<style>
  :root {
    --page-bg: #3c474c;
    --masthead-bg: #ffffff;
    --masthead-ink: #3d5f86;
    --label-ink: #333333;
    --rule-red: #c8102e;
    --band-top: #1b4670;
    --band-blue: #0f3457;
    --band-ink: #e8eef5;
    --photo-light: #a3b1c5;
    --photo-mid: #8597b2;
    --photo-dark: #6f829f;
    --kicker-blue: #bcd2ec;
    --headline-white: #ffffff;
    --agenda-navy: #1b3858;
  }
  html, body { margin: 0; padding: 0; width: 1200px; height: 1125px; overflow: hidden; background: var(--page-bg); }
  .cover {
    position: absolute; left: 197px; top: 27px; width: 807px; height: 1056px;
    overflow: hidden; font-family: "Open Sans", Arial, sans-serif;
  }
  .masthead { position: absolute; left: 0; top: 0; width: 100%; height: 108px; background: var(--masthead-bg); }
  .masthead__title {
    position: absolute; left: 60px; top: 13px; margin: 0;
    font-size: 108px; font-weight: 600; letter-spacing: 2px; color: var(--masthead-ink); line-height: 1;
  }
  .partner { position: absolute; left: 625px; top: 24px; width: 160px; }
  .partner__label { font-size: 10px; font-weight: 600; color: var(--label-ink); letter-spacing: .3px; }
  .partner__name { margin-top: 8px; font-size: 17px; font-weight: 700; line-height: 1.1; color: var(--masthead-ink); }
  .rule { position: absolute; left: 0; width: 100%; }
  .rule--red { top: 108px; height: 8px; background: var(--rule-red); }
  .rule--white { top: 116px; height: 5px; background: var(--masthead-bg); }
  .band {
    position: absolute; left: 0; top: 121px; width: 100%; height: 42px;
    background: linear-gradient(180deg, var(--band-top), var(--band-blue));
  }
  .band__text {
    margin: 0; padding-left: 65px; line-height: 42px; white-space: nowrap;
    font-size: 21px; letter-spacing: .6px; color: var(--band-ink); font-weight: 400;
  }
  .photo {
    position: absolute; left: 0; top: 163px; width: 100%; height: 893px;
    background:
      radial-gradient(ellipse 50% 30% at 50% 78%, #b0bccd 0%, transparent 70%),
      linear-gradient(180deg, var(--photo-mid) 0%, var(--photo-light) 50%, var(--photo-mid) 82%, var(--photo-dark) 100%);
  }
  .teaser { position: absolute; top: 203px; white-space: nowrap; }
  .teaser--left { left: 67px; }
  .teaser--right { left: 394px; }
  .teaser__kicker { margin: 0; font-size: 25px; font-weight: 600; color: var(--kicker-blue); line-height: 1.2; }
  .teaser__title { margin: 0; font-size: 25px; font-weight: 400; color: var(--headline-white); line-height: 1.28; }
  .agenda__word, .agenda__number {
    position: absolute; left: 66px; margin: 0;
    font-family: "Barlow Condensed", "Arial Narrow", sans-serif; font-weight: 700; color: var(--agenda-navy);
    white-space: nowrap;
  }
  .agenda__word { top: 315px; font-size: 76px; line-height: 1; letter-spacing: -.5px; }
  .agenda__number { top: 365px; font-size: 338px; line-height: .8; letter-spacing: -10px; }
  .feature {
    position: absolute; left: 300px; top: 370px; margin: 0; white-space: nowrap;
    font-family: "Barlow Condensed", "Arial Narrow", sans-serif; font-weight: 600;
    font-size: 70px; line-height: 92px; color: var(--headline-white);
    text-shadow: 0 2px 8px rgba(20,40,70,.35);
  }
  .publisher { position: absolute; left: 625px; top: 944px; display: flex; align-items: center; gap: 8px; }
  .publisher__label { font-size: 9px; font-weight: 600; color: var(--headline-white); letter-spacing: .4px; }
  .publisher__name { font-size: 14px; font-weight: 700; color: var(--headline-white); }
</style>
</head>
<body>
  <main class="cover">
    <div class="photo" role="img" aria-label="Close-up photograph of a silver pocket compass lying on a pale blue-grey surface"></div>

    <header class="masthead">
      <h1 class="masthead__title">MRRTN</h1>
      <div class="partner">
        <div class="partner__label">ON BEHALF OF</div>
        <div class="partner__name">Rising Nations<br>Council</div>
      </div>
    </header>
    <div class="rule rule--red"></div>
    <div class="rule rule--white"></div>
    <div class="band"><p class="band__text">MERIDIAN REVIEW OF RISING TRADE NATIONS</p></div>

    <section class="teaser teaser--left">
      <p class="teaser__kicker">CENTRAL ASIA</p>
      <p class="teaser__title">How Bad are<br>Business Environments</p>
    </section>
    <section class="teaser teaser--right">
      <p class="teaser__kicker">ASIAREGIO</p>
      <p class="teaser__title">An Institutional Model<br>to Deepen Integration</p>
    </section>

    <p class="agenda__word">AGENDA</p>
    <p class="agenda__number">21</p>
    <h2 class="feature">WORLD TRADE<br>WITH SUSTAINABLE<br>DEVELOPMENT</h2>

    <footer class="publisher">
      <span class="publisher__label">PUBLISHED BY</span>
      <span class="publisher__name">Quell Press</span>
    </footer>
  </main>
</body>
</html>
```